Revamp of Tessovault.com

If possible, I will select someone who can fully integrate the design into the Wordpress site.
I’m looking for a modern, elegant, interactive revamp of the entire website tessovault.com
### **Main Page**
- **On the top menu**: The 'Sales Figures' option should open the 'Worldwide Albums Sales' and 'Worldwide Singles Sales' pages.
- Improve the **overall design** to look more professional.
- Consider a **better font combination** for improved aesthetics.
- **News Section**: Move above the "Pellorine" section and enhance its appearance.
- **Pellorine Section Carousel**:
- Remove text from images, displaying only the titles.
- Add a header above the carousel: **"All her lyrics in one place."**
- **Four Feature Images ("OKTB," "Sales Figures," etc.)**:
- The 'Sales Figures' section should give users the option to click on either 'Worldwide Albums Sales' or 'Worldwide Singles Sales' for detailed breakdowns.
- Replace with **better graphics** (consider GIFs or subtle animations for a dynamic look).
---
### **Worldwide Albums Sales Page**
- **Redesign the layout** for better visual appeal.
- Make **album displays more interactive, cleaner, and more organized**.
---
### **Worldwide Singles Sales Page**
- Make **single sales displays more interactive, cleaner, and more organized**.
---
### **Pellorine Page**
- **Revamp the entire page** to properly display all posts tagged as "Pellorine."
- **Ensure a functional search bar** is present for this section.
- **Improve overall design and navigation** to enhance user experience.
---
### **OKTB Page**
- **Improve the aesthetics** of the page.
- The **table design must be templated** so that when a new CSV is uploaded, it maintains the same styling.
---
### **Newsletter**
- **Fix the integration issue** where sign-ups are not populating into the newsletter plugin.
---
### **Comments**
- **Implement anti-spam measures** to reduce excessive spam.
---
### **Store**
- **Fix functionality** to ensure everything works properly.
- **Redesign the store layout** for a better shopping experience.
---
### **Flickora Era Page**
- **Revamp this section** for improved design and usability.
---
### **Zandrel Streaming Figures Page**
- **Improve aesthetics** of this section.
- **Ensure the table design is templated** so daily updates maintain the same format when uploaded.
---
### **News Section (Each Article)**
- **Improve the font** for better readability.
- **Use a template** to ensure each article has a **consistent and professional look**.
- **Fix the sidebar** to display the latest five articles in a cleaner, more professional layout.
---
### **Search Button**
- **Fix search functionality**:
- Currently, it returns every page instead of relevant results.
- Ensure it accurately filters and displays relevant content.

```html
<!DOCTYPE html>
<html lang="en">
<head>
<meta charset="utf-8">
<title>Tessovault</title>
<link href="https://fonts.googleapis.com/css2?family=Figtree:wght@400;500;600;700&family=Outfit:wght@500&display=swap" rel="stylesheet">
<style>
:root{
  --paper:#ebe7e0;
  --ink:#161616;
  --muted:#6d6a66;
  --line:#d6d1c8;
  --white:#ffffff;
}
*{box-sizing:border-box;margin:0;padding:0}
html,body{width:1200px;height:1200px;overflow:hidden;background:var(--paper)}
body{font-family:"Figtree",sans-serif;color:var(--ink)}
.page{width:1200px;height:1200px;overflow:hidden;position:relative}

/* top bar */
.topbar{height:50px;display:flex;align-items:center;justify-content:space-between;padding:0 42px;border-bottom:1px solid var(--line)}
.socials{display:flex;gap:14px}
.socials span{width:13px;height:13px;border-radius:50%;background:var(--ink);display:block}
.brand{font-family:"Figtree",sans-serif;font-size:20px;font-weight:500;letter-spacing:3px;display:flex;align-items:center;gap:6px;position:absolute;left:50%;transform:translateX(-50%)}
.brand i{width:8px;height:8px;background:var(--ink);display:block}
.btn-dark{background:var(--ink);color:var(--white);font-size:12px;padding:8px 16px}

/* nav */
.nav{height:50px;display:flex;align-items:center;justify-content:space-between;padding:0 42px;border-bottom:1px solid var(--line)}
.menu{display:flex;gap:38px;font-size:10px;font-weight:600;letter-spacing:1px}
.menu li{list-style:none;display:flex;align-items:center;gap:6px}
.menu li::before{content:"";width:7px;height:7px;border:1px solid var(--ink)}
.menu li.active::before{background:var(--ink)}
.tools{display:flex;align-items:center;gap:20px;font-size:10px;font-weight:600;letter-spacing:1px}
.tools span{display:flex;align-items:center;gap:6px}

/* masthead */
.masthead{height:120px;display:flex;justify-content:space-between;align-items:center;padding:0 40px;border-bottom:1px solid var(--line);font-family:"Outfit",sans-serif;font-size:112px;line-height:1;letter-spacing:1px}

/* hero */
.hero{display:grid;grid-template-columns:264px 552px 264px;gap:0 18px;padding:20px 42px 30px;border-bottom:1px solid var(--line)}
.side-col{display:flex;flex-direction:column;gap:24px}
.card .ph{height:160px}
.card h3{font-size:16.5px;font-weight:500;line-height:1.35;margin:12px 0 10px}
.meta{display:flex;align-items:center;gap:8px;font-size:8.5px;font-weight:600;letter-spacing:1.2px;color:var(--muted)}
.tag{background:var(--ink);color:var(--white);padding:4px 7px;letter-spacing:1.2px}
.lead .ph{height:403px}
.lead .meta{justify-content:center;margin-top:14px}
.lead h2{font-size:22px;font-weight:500;text-align:center;line-height:1.35;margin-top:12px;padding:0 20px}

/* strip */
.strip{display:grid;grid-template-columns:repeat(4,1fr);padding:18px 42px;border-bottom:1px solid var(--line)}
.mini{display:flex;gap:12px;padding-right:18px}
.mini + .mini{border-left:1px solid var(--line);padding-left:18px}
.mini .ph{width:72px;height:78px;flex:none}
.mini h4{font-size:13.5px;font-weight:500;line-height:1.25;margin-bottom:9px}

/* lower */
.lower{display:grid;grid-template-columns:612px 298px;gap:0 78px;padding:40px 0 0 102px}
.post .ph{height:367px}
.profile{border:1px solid var(--line);padding:14px}
.profile .ph{height:150px}
.profile h5{font-size:20px;font-weight:500;text-align:center;margin-top:12px}

.ph{display:block;width:100%}
.g-stage{background:linear-gradient(135deg,#0d1a44,#2c4fb0 45%,#c08a6b 70%,#1a2a6a)}
.g-dark{background:linear-gradient(160deg,#1b1d2a,#3b3f57 55%,#b5906c)}
.g-red{background:linear-gradient(135deg,#2a0c10,#c0272e 45%,#d8a67a 70%,#1b2f2a)}
.g-fur{background:linear-gradient(150deg,#1c2a45,#e8e6e2 50%,#6c7488)}
.g-gold{background:linear-gradient(140deg,#2d1a0c,#d88a2a 45%,#2fa28a)}
.g-skin{background:linear-gradient(135deg,#bfa58a,#7a5a3c)}
.g-glass{background:linear-gradient(135deg,#f3f1ee,#d5d2cd)}
.g-orange{background:linear-gradient(135deg,#6b5a3a,#e4a040)}
.g-brown{background:linear-gradient(135deg,#2a1a12,#8a5a3c)}
.g-satin{background:linear-gradient(135deg,#e9ddc8,#b58a4a 50%,#7a5a30)}
.g-portrait{background:linear-gradient(150deg,#122640,#b88a5c 55%,#27334d)}
</style>
</head>
<body>
<div class="page">
  <header class="topbar">
    <div class="socials" aria-label="Social links"><span></span><span></span><span></span><span></span></div>
    <div class="brand"><i></i>TESSOVAULT</div>
    <div class="btn-dark">Contact Us</div>
  </header>

  <nav class="nav">
    <svg width="16" height="12" viewBox="0 0 16 12"><path d="M1 1h14M1 6h14M1 11h14" stroke="#161616" stroke-width="1.5"/></svg>
    <ul class="menu">
      <li class="active">HOME</li><li>SALES FIGURE</li><li>NEWS</li><li>PELLORINE</li><li>OKTB</li><li>STORE</li>
    </ul>
    <div class="tools">
      <svg width="14" height="14" viewBox="0 0 14 14"><circle cx="6" cy="6" r="4.5" fill="none" stroke="#161616" stroke-width="1.4"/><path d="M9.5 9.5l3.5 3.5" stroke="#161616" stroke-width="1.4"/></svg>
      <svg width="14" height="14" viewBox="0 0 14 14"><circle cx="7" cy="4.5" r="3" fill="none" stroke="#161616" stroke-width="1.3"/><path d="M1.5 13.5c0-3 2.5-5 5.5-5s5.5 2 5.5 5" fill="none" stroke="#161616" stroke-width="1.3"/></svg>
      <span><svg width="13" height="14" viewBox="0 0 13 14"><rect x="1" y="5" width="11" height="8.5" fill="none" stroke="#161616" stroke-width="1.3"/><path d="M4 5V3.5a2.5 2.5 0 015 0V5" fill="none" stroke="#161616" stroke-width="1.3"/></svg>BAG (0)</span>
    </div>
  </nav>

  <div class="masthead"><span>TESSO</span><span>VAULT.</span></div>

  <section class="hero">
    <div class="side-col">
      <article class="card"><div class="ph g-dark" role="img" aria-label="Singer performing on stage in a dark sparkling dress"></div><h3>Quick and Healthy Meals for Busy Weeknights</h3><div class="meta"><span class="tag">METRO</span>DEC 19, 2024</div></article>
      <article class="card"><div class="ph g-fur" role="img" aria-label="Singer in a white fur coat singing into a microphone"></div><h3>The Perfect Morning Skin Care Routine for Every Skin Type</h3><div class="meta"><span class="tag">METRO</span>DEC 19, 2024</div></article>
    </div>
    <article class="lead"><div class="ph g-stage" role="img" aria-label="Singer in a red dress performing under blue stage lights"></div><div class="meta"><span class="tag">METRO</span>DEC 19, 2024</div><h2>Why Double Cleansing Is a Game-Changer for Your Skin</h2></article>
    <div class="side-col">
      <article class="card"><div class="ph g-red" role="img" aria-label="Singer on stage in front of red lights"></div><h3>Simple Ways to Make Your Lifestyle More Eco-Friendly</h3><div class="meta"><span class="tag">METRO</span>DEC 19, 2024</div></article>
      <article class="card"><div class="ph g-gold" role="img" aria-label="Portrait of the singer in warm golden light"></div><h3>The Ultimate Guide to Balanced Meal Planning</h3><div class="meta"><span class="tag">METRO</span>DEC 19, 2024</div></article>
    </div>
  </section>

  <section class="strip">
    <article class="mini"><div class="ph g-skin" role="img" aria-label="Face mask skincare close-up"></div><div><h4>The Importance of Sleep for Healthy Skin</h4><div class="meta"><span class="tag">SKIN CARE</span>OCT 30, 2024</div></div></article>
    <article class="mini"><div class="ph g-glass" role="img" aria-label="Drop of water on a glass surface"></div><div><h4>Elevate Your Everyday: Tips for a Balanced Lifestyle</h4><div class="meta"><span class="tag">FEATURED</span>OCT 30, 2024</div></div></article>
    <article class="mini"><div class="ph g-orange" role="img" aria-label="Sliced citrus fruit"></div><div><h4>Small Changes, Big Impact: Redefining Your Daily Routine</h4><div class="meta"><span class="tag">BEAUTY</span>OCT 30, 2024</div></div></article>
    <article class="mini"><div class="ph g-brown" role="img" aria-label="Close-up of skin in warm light"></div><div><h4>Glow Inside and Out: Secrets to Radiant Health</h4><div class="meta"><span class="tag">SKIN CARE</span>OCT 30, 2024</div></div></article>
  </section>

  <section class="lower">
    <article class="post"><div class="ph g-satin" role="img" aria-label="Singer reclining in a gold satin dress"></div></article>
    <aside class="profile"><div class="ph g-portrait" role="img" aria-label="Portrait of the content writer"></div><h5>Liam Dailey</h5></aside>
  </section>
</div>
</body>
</html>
```